Business Card Design Project for Heron Crest Lending

Hello there,

We are looking for a business card design for our new Heron Crest Lending car financing company. We are looking for a business card that will include:

- An address
- Telephone number and extension
- Employee Name
- Employee Title
- Our logo and name clearly visible

We are including our logo with this writeup, we are looking to convey friendliness, trus and memorability. Colors and everything else is up to you.

Target Market(s)

18-34 year old males and females

Industry/Entity Type

Business

```html
<!DOCTYPE html>
<html lang="en">
<head>
<meta charset="utf-8">
<title>Heron Crest Lending — Business Card</title>
<link rel="stylesheet" href="https://fonts.googleapis.com/css2?family=Cinzel:wght@600&family=Open+Sans:wght@400;700&display=swap">
<style>
  :root {
    --navy: #1a3a7c;
    --white: #ffffff;
    --stage: #e4e2df;
    --ink-light: #f4f6fb;
  }
  * { margin: 0; padding: 0; box-sizing: border-box; }
  html, body { width: 1200px; height: 594px; overflow: hidden; }
  body {
    background: var(--stage);
    position: relative;
    font-family: "Open Sans", Arial, sans-serif;
  }
  .card {
    position: absolute;
    top: 149px;
    width: 520px;
    height: 296px;
    border-radius: 16px;
    overflow: hidden;
    background: var(--white);
    box-shadow: 0 6px 18px rgba(0,0,0,.18);
  }
  .card--front { left: 50px; }
  .card--back { left: 630px; }

  .brand {
    position: absolute;
    color: var(--navy);
    font-family: "Cinzel", "Times New Roman", serif;
    font-weight: 600;
    text-align: center;
    line-height: 1;
    white-space: nowrap;
  }
  .brand__name { display: block; font-size: 40px; letter-spacing: 3px; }
  .brand__sub { display: block; font-size: 17px; letter-spacing: 11px; margin-top: 8px; padding-left: 11px; }

  .card--front .brand { left: 0; right: 0; top: 86px; }

  .front-band { position: absolute; left: 0; right: 0; top: 196px; bottom: 0; }
  .stripe { position: absolute; left: 0; right: 0; height: 5px; background: var(--navy); }
  .stripe--one { top: 0; }
  .stripe--two { top: 9px; }
  .front-band__solid {
    position: absolute; left: 0; right: 0; top: 18px; bottom: 0;
    background: var(--navy);
    display: flex; align-items: center; justify-content: center;
  }
  .website {
    color: var(--white);
    font-family: "Cinzel", "Times New Roman", serif;
    font-weight: 600;
    font-size: 17px;
    letter-spacing: 2px;
  }

  .card--back .brand { left: 10px; width: 270px; top: 72px; }
  .card--back .brand__name { font-size: 30px; letter-spacing: 2px; }
  .card--back .brand__sub { font-size: 13px; letter-spacing: 8px; margin-top: 7px; padding-left: 8px; }
  .address {
    position: absolute; left: 36px; top: 150px;
    color: var(--navy);
    font-family: "Cinzel", "Times New Roman", serif;
    font-weight: 600;
    font-size: 13px;
    line-height: 1.3;
    white-space: nowrap;
  }
  .vstripe { position: absolute; top: 0; bottom: 0; width: 6px; background: var(--navy); }
  .vstripe--one { left: 290px; }
  .vstripe--two { left: 301px; }
  .back-panel {
    position: absolute; left: 312px; right: 0; top: 0; bottom: 0;
    background: var(--navy);
    color: var(--ink-light);
  }
  .person { position: absolute; right: 22px; top: 58px; text-align: right; }
  .person__name { font-weight: 700; font-size: 13px; letter-spacing: 1px; }
  .person__title { font-size: 12px; }
  .contacts { position: absolute; right: 18px; top: 184px; list-style: none; }
  .contact {
    display: flex; justify-content: flex-end; align-items: center; gap: 8px;
    font-size: 12px; height: 27px; white-space: nowrap;
  }
  .contact__icon { width: 20px; height: 20px; display: block; flex: none; }
</style>
</head>
<body>
  <section class="card card--front" aria-label="Card front">
    <div class="brand">
      <span class="brand__name">HERON CREST</span>
      <span class="brand__sub">LENDING</span>
    </div>
    <div class="front-band">
      <div class="stripe stripe--one"></div>
      <div class="stripe stripe--two"></div>
      <div class="front-band__solid">
        <span class="website">WWW.HERONCREST.COM</span>
      </div>
    </div>
  </section>

  <section class="card card--back" aria-label="Card back">
    <div class="brand">
      <span class="brand__name">HERON CREST</span>
      <span class="brand__sub">LENDING</span>
    </div>
    <p class="address">4820 ALDER RD FAIRVIEW<br>CA 95812</p>
    <div class="vstripe vstripe--one"></div>
    <div class="vstripe vstripe--two"></div>
    <div class="back-panel">
      <div class="person">
        <p class="person__name">MARCUS AVERY</p>
        <p class="person__title">Owner</p>
      </div>
      <ul class="contacts">
        <li class="contact">
          <span>555-204-3187</span>
          <svg class="contact__icon" viewBox="0 0 20 20" aria-hidden="true">
            <rect width="20" height="20" rx="4" fill="#fff"/>
            <path d="M6 5h2.5l1 3-1.5 1a7 7 0 0 0 3 3l1-1.5 3 1V14a1.5 1.5 0 0 1-1.5 1.5A9 9 0 0 1 4.5 6.5 1.5 1.5 0 0 1 6 5z" fill="#1a3a7c"/>
          </svg>
        </li>
        <li class="contact">
          <span>800-555-0172</span>
          <svg class="contact__icon" viewBox="0 0 20 20" aria-hidden="true">
            <rect width="20" height="20" rx="4" fill="#fff"/>
            <path d="M4 8c0-2 2.5-3 6-3s6 1 6 3v1.5h-3V8H7v1.5H4z" fill="#1a3a7c"/>
            <rect x="5" y="11" width="10" height="4.5" rx="1" fill="#1a3a7c"/>
          </svg>
        </li>
        <li class="contact">
          <span>marcus@heroncrest.com</span>
          <svg class="contact__icon" viewBox="0 0 20 20" aria-hidden="true">
            <rect width="20" height="20" rx="4" fill="#fff"/>
            <rect x="4" y="6" width="12" height="8.5" fill="none" stroke="#1a3a7c" stroke-width="1.5"/>
            <path d="M4 6l6 5 6-5" fill="none" stroke="#1a3a7c" stroke-width="1.5"/>
          </svg>
        </li>
      </ul>
    </div>
  </section>
</body>
</html>
```